Letterhead

We would like to use the logo attached as a new letterhead. Our problem is that we think the dark blue background is too much. We'd like a sleek, professional letterhead, and we'd like at least five options to choose from. I've also uploaded our old letterhead for reference of the style we're going for.

```html
<!DOCTYPE html>
<html lang="en">
<head>
<meta charset="utf-8">
<title>Northvale Group Letterhead</title>
<link href="https://fonts.googleapis.com/css2?family=Tinos:wght@400;700&display=swap" rel="stylesheet">
<style>
  :root {
    --backdrop: #e6e6e6;
    --paper: #ffffff;
    --brand-blue: #4a64b4;
    --brand-gold: #c9a350;
    --ink: #3b4f91;
    --ink-soft: #5a6da8;
  }
  * { margin: 0; padding: 0; box-sizing: border-box; }
  html, body { width: 1200px; height: 638px; overflow: hidden; background: var(--backdrop); }
  body { font-family: "Tinos", "Times New Roman", serif; color: var(--ink); }
  .letterhead {
    position: absolute; left: 394px; top: 19px;
    width: 412px; height: 600px;
    background: var(--paper);
    box-shadow: 0 1px 4px rgba(0,0,0,.18);
  }
  .brand {
    position: absolute; left: 18px; top: 22px;
    display: flex; align-items: center; gap: 7px;
  }
  .brand-mark { width: 20px; height: 20px; background: var(--brand-gold); }
  .brand-name {
    font-weight: 700; font-size: 17px; line-height: 1; color: var(--brand-blue);
    letter-spacing: .3px;
  }
  .contact {
    position: absolute; right: 16px; top: 28px;
    text-align: right; font-size: 6px; line-height: 8.5px;
    color: var(--ink); text-decoration: underline;
  }
  .contact-bar {
    position: absolute; right: 4px; top: 26px; width: 8px; height: 28px;
    background: var(--brand-blue); border-left: 3px solid var(--brand-gold);
  }
  .letter-body {
    position: absolute; left: 28px; top: 184px; width: 352px;
    font-size: 6.4px; line-height: 8.6px; color: var(--ink);
  }
  .salutation { font-size: 8.5px; margin-bottom: 16px; text-decoration: underline; }
  .letter-body p.para { margin-bottom: 9px; text-align: justify; text-decoration: underline; }
  .closing { margin-top: 16px; text-decoration: underline; }
  .signature {
    display: block; width: 56px; height: 14px; margin-top: 20px;
    background: linear-gradient(90deg, var(--ink-soft), var(--ink));
    border-radius: 7px; opacity: .55;
  }
  .footer {
    position: absolute; left: 0; right: 0; bottom: 6px;
    text-align: center; font-size: 5.5px; color: var(--ink);
  }
</style>
</head>
<body>
  <main class="letterhead">
    <header>
      <div class="brand">
        <span class="brand-mark"></span>
        <span class="brand-name">NORTHVALE GROUP</span>
      </div>
      <div class="contact">
        044-555 0192<br>
        info@northvale.com<br>
        www.northvale.com
      </div>
      <div class="contact-bar"></div>
    </header>

    <section class="letter-body">
      <p class="salutation">Dear Mr. Carter,</p>
      <p class="para">Lorem ipsum dolor sit amet, consectetuer adipiscing elit, sed diam nonummy nibh euismod tincidunt ut laoreet dolore magna aliquam erat volutpat. Ut wisi enim ad minim veniam, quis nostrud exerci tation ullamcorper suscipit lobortis nisl ut aliquip ex ea commodo consequat. Duis autem vel eum iriure dolor in hendrerit in vulputate velit esse molestie consequat, vel illum dolore eu feugiat.</p>
      <p class="para">Lorem ipsum dolor sit amet, consectetuer adipiscing elit, sed diam nonummy nibh euismod tincidunt ut laoreet dolore magna aliquam erat volutpat. Ut wisi enim ad minim veniam, quis nostrud exerci tation ullamcorper suscipit lobortis nisl ut aliquip ex ea commodo consequat. Duis autem vel eum iriure dolor in hendrerit in vulputate velit esse molestie.</p>
      <p class="para">Lorem ipsum dolor sit amet, consectetuer adipiscing elit, sed diam nonummy nibh euismod tincidunt ut laoreet dolore magna aliquam erat volutpat. Ut wisi enim ad minim veniam, quis nostrud exerci tation ullamcorper suscipit lobortis nisl ut aliquip ex ea commodo consequat. Duis autem vel eum iriure dolor in hendrerit in suscipit lobortis nisl ut aliquip ex ea commodo consequat. Duis autem vel eum iriure dolor in hendrerit in vulputate velit esse molestie consequat, vel illum.</p>
      <p class="para">Lorem ipsum dolor sit amet, consectetuer adipiscing elit, sed diam nonummy nibh euismod tincidunt ut laoreet dolore magna aliquam erat volutpat. Ut wisi enim ad minim veniam, quis nostrud exerci tation ullamcorper suscipit lobortis nisl ut aliquip ex ea commodo consequat. Duis autem vel eum iriure dolor in.</p>
      <p class="closing">Sincerely,</p>
      <span class="signature" role="img" aria-label="Handwritten signature"></span>
    </section>

    <footer class="footer">Your Address, City, State, Zip 0000</footer>
  </main>
</body>
</html>
```